International Film making Business needs the 5 Logos provided made into a POSTER Format

Design Task:
CREATE A POSTER DESIGN USING THE 5 LOGOS PROVIDED. The GLAD SKY VISTA LOGO should stand out from the others by being in the middle with the other 4 logos connected to it somehow.

The 5 Businesses already has their 5 Logos, all similar in design to each other.

GLAD SKY VISTA is the Main Logo that encompasses the other 4 Logos. So it must stand out more and it is like the Overall Business entity that incorporates the other 4 Logos.

What is required is that by using the 5 Logo designs provided, create a cool graphic artwork that somehow incorporates ALL of the 5 Logos - But having the GLAD SKY VISTA Logo at the forefront/most important/standing out the most.
- GLAD SKY VISTA will probably be bigger than the others
- and could be changed into 3D.

I have attached all 5 logos and a hand drawn example of how the GLAD SKY VISTAS could stand out from the rest.

THE DESIGNS OF THE LOGOS SHOULD NOT BE CHANGED (except the GLADSKYVISTA which can be 3D)

Please do not be restricted with the sample idea. Creativity is encouraged

DIMENSION: 3000 mm x 6000 mm
high resolution graphic

Logo Text

glad sky , glad sky reels, glad sky tales, glad sky groovy, GLAD SKY VISTAS

Requirements
Must have
• USE THE 5 LOGOS PROVIDED ONLY - Only GLAD SKY VISTA can be changed into 3D only
Nice to have
• Eye catching design, showing the Glad Sky Vista as the most powerful Logo that has the other 4 as subordinate companies
Should not have
• ANY CHANGE IN THE 5 LOGO DESIGNS (EXcept 3D for Glad Sky Vistas)

```html
<!DOCTYPE html>
<html lang="en">
<head>
<meta charset="utf-8">
<title>Glad Sky Vistas Poster</title>
<link rel="stylesheet" href="https://fonts.googleapis.com/css2?family=Cinzel:wght@500;600&family=Montserrat:wght@300&display=swap">
<style>
  :root {
    --paper-grey: #d0d0d3;
    --night: #131416;
    --film-black: #000000;
    --frame-white: #ffffff;
    --gold: #c9a13e;
    --gold-deep: #a87d22;
    --url-grey: #9b9b9d;
    --brand-blue: #2a86d6;
    --brand-charcoal: #262626;
    --brand-red: #cf2f3a;
    --brand-green: #2f9a1d;
  }
  html, body {
    margin: 0;
    padding: 0;
    width: 1200px;
    height: 600px;
    overflow: hidden;
    background: var(--paper-grey);
  }
  .poster {
    display: block;
    width: 1200px;
    height: 600px;
  }
  .brand-name {
    font-family: "Cinzel", serif;
    font-weight: 600;
    text-anchor: middle;
  }
  .sub-blue { fill: var(--brand-blue); }
  .sub-charcoal { fill: var(--brand-charcoal); }
  .sub-red { fill: var(--brand-red); }
  .sub-green { fill: var(--brand-green); }
  .main-name {
    font-family: "Cinzel", serif;
    font-weight: 500;
    fill: var(--gold);
  }
  .main-url {
    font-family: "Montserrat", sans-serif;
    font-weight: 300;
    fill: var(--url-grey);
  }
</style>
</head>
<body>
<svg class="poster" viewBox="0 0 1200 600" xmlns="http://www.w3.org/2000/svg">
  <defs>
    <linearGradient id="projector-tone" x1="0" y1="0" x2="0" y2="1">
      <stop offset="0" stop-color="#1a1b1d"/>
      <stop offset="1" stop-color="#0c0c0d"/>
    </linearGradient>
  </defs>

  <rect class="backdrop" width="1200" height="600" fill="var(--paper-grey)"/>

  <polygon class="projector-beam" points="452,338 1200,219 1200,600 499,600 387,527 370,422" fill="var(--night)"/>

  <g class="film-strip" transform="translate(0 100) rotate(-9.4)">
    <rect class="film-band" role="img" aria-label="Black film strip with sprocket holes along both edges" x="-60" y="0" width="1400" height="306" fill="var(--film-black)"/>

    <g class="frame">
      <rect x="42" y="55" width="250" height="200" fill="var(--frame-white)"/>
      <text class="brand-name sub-blue" x="170" y="150" font-size="28">GLAD</text>
      <text class="brand-name sub-blue" x="170" y="182" font-size="28">SKY</text>
    </g>
    <g class="frame">
      <rect x="307" y="55" width="250" height="200" fill="var(--frame-white)"/>
      <text class="brand-name sub-charcoal" x="432" y="150" font-size="20">GLAD SKY</text>
      <text class="brand-name sub-charcoal" x="432" y="180" font-size="28">REELS</text>
    </g>
    <g class="frame">
      <rect x="566" y="55" width="250" height="200" fill="var(--frame-white)"/>
      <text class="brand-name sub-red" x="691" y="145" font-size="20">GLAD SKY</text>
      <text class="brand-name sub-red" x="691" y="175" font-size="26">TALES</text>
    </g>
    <g class="frame">
      <rect x="830" y="55" width="250" height="200" fill="var(--frame-white)"/>
      <text class="brand-name sub-green" x="955" y="160" font-size="20">GLAD SKY</text>
      <text class="brand-name sub-green" x="955" y="192" font-size="28">GROOVY</text>
    </g>
    <rect class="frame" x="1100" y="55" width="250" height="200" fill="var(--frame-white)"/>
  </g>

  <rect class="film-projector" role="img" aria-label="Film projector with two reels" x="58" y="280" width="284" height="290" rx="40" fill="url(#projector-tone)"/>

  <circle class="main-mark" cx="640" cy="440" r="95" fill="var(--gold-deep)"/>

  <g class="main-brand">
    <text class="main-name" x="765" y="455" font-size="64" textLength="377" lengthAdjust="spacingAndGlyphs">GLAD SKY</text>
    <text class="main-name" x="765" y="522" font-size="64" textLength="377" lengthAdjust="spacingAndGlyphs">VISTAS</text>
    <text class="main-url" x="765" y="553" font-size="25" textLength="377" lengthAdjust="spacingAndGlyphs">gladskyvistas.com.au</text>
  </g>
</svg>
</body>
</html>
```